Brindale transport business cards

Front of card, Looking for my logo on one side of the card

Back of card,
Brindale Transport Maintenance
Onsite Cars, Trucks & trailer maintenance and repairs
Ronan Brindale
0452819036
Brindaletm@fernmail.com

```html
<!DOCTYPE html>
<html lang="en">
<head>
<meta charset="utf-8">
<title>Brindale Transport Maintenance – Business Card</title>
<link href="https://fonts.googleapis.com/css2?family=Poppins:wght@400;600;700&display=swap" rel="stylesheet">
<style>
  :root {
    --page-bg: #e9e6e6;
    --card-light: #f3eded;
    --card-light-edge: #ebe1e1;
    --card-dark: #000000;
    --brand-blue: #0b7bd6;
    --name-blue: #1289e8;
    --ink: #111111;
    --white: #ffffff;
  }
  * { margin: 0; padding: 0; box-sizing: border-box; }
  html, body {
    width: 1200px;
    height: 900px;
    overflow: hidden;
    background: var(--page-bg);
    font-family: "Poppins", sans-serif;
  }
  .business-card {
    position: absolute;
    left: 100px;
    top: 141px;
    width: 1000px;
    height: 618px;
    display: grid;
    grid-template-columns: 507px 7px 1fr;
    grid-template-rows: 1fr 89px;
    box-shadow: 0 10px 30px rgba(0,0,0,0.18);
  }
  .brand-panel {
    grid-column: 1;
    grid-row: 1;
    background: radial-gradient(ellipse at 50% 55%, var(--card-light) 40%, var(--card-light-edge) 100%);
    display: flex;
    align-items: center;
    justify-content: center;
    padding-top: 20px;
  }
  .brand-mark {
    display: flex;
    align-items: center;
    gap: 14px;
  }
  .brand-square {
    width: 34px;
    height: 34px;
    background: var(--brand-blue);
  }
  .brand-name {
    font-weight: 700;
    font-size: 27px;
    line-height: 1.15;
    color: var(--ink);
  }
  .divider {
    grid-column: 2;
    grid-row: 1;
    background: var(--brand-blue);
  }
  .contact-panel {
    grid-column: 3;
    grid-row: 1;
    background: var(--card-dark);
    padding: 226px 0 0 60px;
    color: var(--white);
  }
  .person-name {
    font-weight: 600;
    font-size: 38px;
    line-height: 1;
    color: var(--name-blue);
    letter-spacing: 0.2px;
    margin-bottom: 52px;
  }
  .contact-line {
    display: flex;
    align-items: center;
    gap: 12px;
    font-size: 28px;
    line-height: 37px;
  }
  .contact-line svg { width: 28px; height: 28px; flex: none; }
  .tagline-band {
    grid-column: 1 / 4;
    grid-row: 2;
    background: var(--brand-blue);
    color: var(--white);
    font-weight: 700;
    font-size: 28px;
    display: flex;
    align-items: center;
    padding-left: 100px;
    padding-bottom: 6px;
  }
</style>
</head>
<body>
  <div class="business-card">
    <section class="brand-panel">
      <div class="brand-mark">
        <span class="brand-square"></span>
        <span class="brand-name">Brindale Transport<br>Maintenance</span>
      </div>
    </section>
    <div class="divider"></div>
    <section class="contact-panel">
      <h1 class="person-name">RONAN BRINDALE</h1>
      <p class="contact-line">
        <svg viewBox="0 0 24 24" aria-hidden="true"><path fill="var(--name-blue)" d="M6.6 10.8a15.1 15.1 0 0 0 6.6 6.6l2.2-2.2c.3-.3.7-.4 1-.2 1.1.4 2.3.6 3.6.6.6 0 1 .4 1 1V20c0 .6-.4 1-1 1A17 17 0 0 1 3 4c0-.6.4-1 1-1h3.5c.6 0 1 .4 1 1 0 1.3.2 2.5.6 3.6.1.3 0 .7-.2 1z"/><path fill="none" stroke="var(--name-blue)" stroke-width="1.8" d="M14 3.5a7 7 0 0 1 6.5 6.5M14 7a3.5 3.5 0 0 1 3 3"/></svg>
        <span>0452819036</span>
      </p>
      <p class="contact-line">
        <svg viewBox="0 0 24 24" aria-hidden="true"><rect x="2" y="5" width="20" height="14" fill="var(--name-blue)"/><path d="M2 5l10 8 10-8M2 19l7-7M22 19l-7-7" fill="none" stroke="var(--card-dark)" stroke-width="1.5"/></svg>
        <span>Brindaletm@fernmail.com</span>
      </p>
    </section>
    <footer class="tagline-band">Onsite Cars, Trucks &amp; Trailer maintenance and repairs</footer>
  </div>
</body>
</html>
```